Signage Design Project

Busisness is a bakery and deli long time owned by the Tavel family. Want to develop a new outside sign that communicates it is a deli and a bakery but keeps the tavel name in the design.

The sign when produced will be about 10' by 3' . It is not lighted at present but could be if it were advantageous.

The name of the store is:

Tavel's Hudson Bakery and Deli. The concept is to have a new,modern sign that reinforces that it is a deli and a bakery, as most people only know about the bakery side of the business
Updates

The name Tavel is just a reinforcer so the people kno it is still in the family.  The emphasis should be on the HUDSON BAKERY and DELI

Target Market(s)

Small business breakfast and lunch customers

Industry/Entity Type

Bakery

Requirements
Must have
• Great impact from the road. Communicate that it is a deli and a bakery. Keep the Tavel name but need not be a major design element

```html
<!DOCTYPE html>
<html lang="en">
<head>
<meta charset="utf-8">
<title>Tavel's Hudson Bakery and Deli – Storefront Sign</title>
<link rel="stylesheet" href="https://fonts.googleapis.com/css2?family=Arimo:wght@700&display=swap">
<style>
  :root {
    --page-bg: #efedea;
    --purple-dark: #7d46a6;
    --purple-light: #a877c8;
    --orange-dark: #bf6630;
    --orange-light: #e49a57;
    --accent-pink: #e8769e;
    --sign-white: #ffffff;
    --frame: #f7f2ee;
  }
  html, body {
    margin: 0;
    padding: 0;
    width: 1200px;
    height: 773px;
    overflow: hidden;
    background: var(--page-bg);
  }
  .sign-stage {
    width: 1200px;
    height: 773px;
    display: flex;
    align-items: center;
    justify-content: center;
  }
  .storefront-sign {
    width: 1160px;
    height: 352px;
    display: block;
    box-shadow: 0 6px 18px rgba(0, 0, 0, 0.18);
  }
  .sign-text {
    font-family: "Arimo", sans-serif;
    font-weight: 700;
    fill: var(--sign-white);
  }
</style>
</head>
<body>
<main class="sign-stage">
  <svg class="storefront-sign" viewBox="0 0 1160 352" role="img" aria-label="Tavel's Hudson Bakery and Deli sign">
    <defs>
      <linearGradient id="purple-band" x1="0" y1="0" x2="1" y2="0">
        <stop offset="0" stop-color="var(--purple-dark)"/>
        <stop offset="1" stop-color="var(--purple-light)"/>
      </linearGradient>
      <linearGradient id="orange-band" x1="0" y1="0" x2="0" y2="1">
        <stop offset="0" stop-color="var(--orange-light)"/>
        <stop offset="1" stop-color="var(--orange-dark)"/>
      </linearGradient>
    </defs>

    <rect class="sign-frame" x="0" y="0" width="1160" height="352" fill="var(--frame)"/>
    <rect class="band-top" x="6" y="6" width="1148" height="180" fill="url(#purple-band)"/>
    <rect class="band-bottom" x="6" y="186" width="1148" height="160" fill="url(#orange-band)"/>

    <circle class="family-marker" cx="62" cy="96" r="16" fill="var(--accent-pink)"/>
    <text class="sign-text family-name" x="92" y="118" font-size="60">Tavel</text>
    <text class="sign-text place-name" x="720" y="140" font-size="118" text-anchor="middle">Hudson</text>
    <text class="sign-text trade-line" x="580" y="312" font-size="122" text-anchor="middle" textLength="1060" lengthAdjust="spacingAndGlyphs">BAKERY &amp; DELI</text>
  </svg>
</main>
</body>
</html>
```